Biz Card for Harrowfield Property Partners - HWPP

Harrowfield Property Partners is a commercial real estate acquisitions firm. We buy commercial property and need to raise capital from investors for each deal we buy. The vibe needs to be: give us your money, we will multiply it.
Our website: www.hrwpp-example.com
Competitors are: https://velmarholdings-example.com/, https://tribanquepartners-example.com/, http://www.ostrellecapital-example.com/
Target Market(s)
High Net Worth Individuals, Bankers, Insurance Companies, Commercial Real Estate Brokers.
Industry/Entity Type
Investment Banking
Contact Information for Business Card
Name, Title, Addess, Cell#, Office#, email, website
Requirements
Must have
- use one of our logos. See website for look and feel: www.hrwpp-example.com
Nice to have
- see website: www.hrwpp-example.com

```html
<!DOCTYPE html>
<html lang="en">
<head>
<meta charset="utf-8">
<title>Harrowfield Property Partners – Business Card</title>
<link rel="stylesheet" href="https://fonts.googleapis.com/css2?family=Lato:wght@400&family=Montserrat:wght@400;500;600&display=swap">
<style>
  :root {
    --stage: #e8e8e8;
    --navy: #07344e;
    --navy-deep: #03223a;
    --paper: #f7f7f7;
    --white: #ffffff;
    --shadow: rgba(0, 0, 0, 0.28);
  }
  * { margin: 0; padding: 0; box-sizing: border-box; }
  html, body { width: 1200px; height: 1200px; overflow: hidden; }
  body { background: var(--stage); position: relative; font-family: "Montserrat", sans-serif; }

  .card {
    position: absolute;
    left: 262px;
    width: 686px;
    height: 392px;
    border-radius: 17px;
    overflow: hidden;
    box-shadow: 0 14px 22px var(--shadow);
  }
  .card--front { top: 165px; background: var(--paper); }
  .card--back {
    top: 653px;
    background: linear-gradient(180deg, var(--navy) 0%, var(--navy-deep) 100%);
  }

  .front-panel { position: absolute; inset: 0; width: 100%; height: 100%; }

  .brand-mark {
    position: absolute;
    border-radius: 50%;
  }
  .brand-name, .brand-sub {
    position: absolute;
    font-family: "Lato", sans-serif;
    font-weight: 400;
    white-space: nowrap;
    text-transform: uppercase;
    line-height: 1;
  }

  /* front logo block */
  .front-logo .brand-mark { left: 106px; top: 102px; width: 74px; height: 74px; background: var(--navy); }
  .front-logo .brand-name {
    left: 0; width: 286px; top: 186px; text-align: center;
    font-size: 25px; letter-spacing: 3px; color: var(--navy);
  }
  .front-logo .brand-sub {
    left: 0; width: 286px; top: 220px; text-align: center;
    font-size: 10.5px; letter-spacing: 3px; color: var(--navy);
  }

  /* contact block */
  .contact { position: absolute; left: 481px; top: 104px; color: var(--white); }
  .contact__name { font-size: 20px; font-weight: 600; letter-spacing: 0.3px; line-height: 1.1; }
  .contact__title { font-size: 14px; font-weight: 400; margin-top: 2px; }
  .contact__address { font-size: 14px; line-height: 19px; margin-top: 12px; }
  .contact__list { list-style: none; margin-top: 11px; }
  .contact__list li {
    display: flex; align-items: center; gap: 8px;
    font-size: 14px; line-height: 20px;
  }
  .contact__list svg { width: 12px; height: 12px; flex: none; fill: var(--white); }

  /* back */
  .back-logo .brand-mark { left: 101px; top: 137px; width: 118px; height: 118px; background: var(--white); }
  .back-logo .brand-name {
    left: 239px; top: 164px; font-size: 40px; letter-spacing: 4px; color: var(--white);
  }
  .back-logo .brand-sub {
    left: 241px; top: 215px; font-size: 16px; letter-spacing: 4.2px; color: var(--white);
  }
  .back-web {
    position: absolute; left: 0; width: 100%; top: 268px; text-align: center;
    font-size: 15px; font-weight: 500; letter-spacing: 4px; color: var(--white);
  }
</style>
</head>
<body>

<section class="card card--front" aria-label="Business card front">
  <svg class="front-panel" viewBox="0 0 686 392" preserveAspectRatio="none" aria-hidden="true">
    <defs>
      <linearGradient id="navyFade" x1="0" y1="0" x2="0" y2="1">
        <stop offset="0" stop-color="#07344e"/>
        <stop offset="1" stop-color="#03223a"/>
      </linearGradient>
    </defs>
    <polygon points="382,0 686,0 686,392 410,392" fill="url(#navyFade)"/>
  </svg>

  <div class="front-logo">
    <span class="brand-mark" aria-hidden="true"></span>
    <span class="brand-name">Harrowfield</span>
    <span class="brand-sub">Property Partners</span>
  </div>

  <div class="contact">
    <p class="contact__name">DANIEL WHITCOMBE</p>
    <p class="contact__title">President</p>
    <p class="contact__address">418 Larkmoor Ave, Suite 902<br>Westbrook, FL 33190</p>
    <ul class="contact__list">
      <li>
        <svg viewBox="0 0 24 24" aria-label="Office"><path d="M6.6 10.8a15.1 15.1 0 0 0 6.6 6.6l2.2-2.2a1 1 0 0 1 1-.25 11.4 11.4 0 0 0 3.6.57 1 1 0 0 1 1 1V20a1 1 0 0 1-1 1A17 17 0 0 1 3 4a1 1 0 0 1 1-1h3.5a1 1 0 0 1 1 1c0 1.25.2 2.45.57 3.57a1 1 0 0 1-.25 1z"/></svg>
        (555) 214-7730
      </li>
      <li>
        <svg viewBox="0 0 24 24" aria-label="Cell"><path d="M7 1h10a2 2 0 0 1 2 2v18a2 2 0 0 1-2 2H7a2 2 0 0 1-2-2V3a2 2 0 0 1 2-2zm0 3v14h10V4zm5 15.5a1 1 0 1 0 0 2 1 1 0 0 0 0-2z"/></svg>
        (555) 382-6041
      </li>
      <li>
        <svg viewBox="0 0 24 24" aria-label="Email"><path d="M2 5h20v14H2zm2 2v.5l8 5 8-5V7zm0 2.9V17h16V9.9l-8 5z"/></svg>
        info@hrwpp-example.com
      </li>
      <li>
        <svg viewBox="0 0 24 24" aria-label="Website"><path d="M12 2a10 10 0 1 0 0 20 10 10 0 0 0 0-20zm6.9 6h-2.9a15.6 15.6 0 0 0-1.4-3.6A8 8 0 0 1 18.9 8zM12 4c.8 1.2 1.5 2.5 1.9 4h-3.8c.4-1.5 1.1-2.8 1.9-4zM4.3 14a8 8 0 0 1 0-4h3.4a16 16 0 0 0 0 4zm.8 2h2.9c.3 1.3.8 2.5 1.4 3.6A8 8 0 0 1 5.1 16zM8 8H5.1a8 8 0 0 1 4.3-3.6C8.8 5.5 8.3 6.7 8 8zm4 12c-.8-1.2-1.5-2.5-1.9-4h3.8c-.4 1.5-1.1 2.8-1.9 4zm2.3-6H9.7a14.7 14.7 0 0 1 0-4h4.6a14.7 14.7 0 0 1 0 4zm.3 5.6c.6-1.1 1.1-2.3 1.4-3.6h2.9a8 8 0 0 1-4.3 3.6zm1.7-5.6a16 16 0 0 0 0-4h3.4a8 8 0 0 1 0 4z"/></svg>
        www.hrwpp-example.com
      </li>
    </ul>
  </div>
</section>

<section class="card card--back" aria-label="Business card back">
  <div class="back-logo">
    <span class="brand-mark" aria-hidden="true"></span>
    <span class="brand-name">Harrowfield</span>
    <span class="brand-sub">Property Partners</span>
  </div>
  <p class="back-web">www.hrwpp-example.com</p>
</section>

</body>
</html>
```